Marlow Crest Group (Real Estate and Investment)

A high end, clean design.
We are a real estate company with sales, asset management and investment divisions. We want to use a black and white scheme which is really high end feel. The back of the card can just be the logo (black background with the white writing) as we will probably emboss this when we print)

Target Market(s)

High level investors, high end houses for sale

Industry/Entity Type

Business

Contact Information for Business Card

Name, position, phone number and email address
Glen Varley, Managing Director, 0437259064 and glen@marlowcrest-example.com.au

Requirements
Must have
• Back of the card to be the black background with the white writing (as per the attached images). Would like the capacity to emboss the writing and logo

```html
<!DOCTYPE html>
<html lang="en">
<head>
<meta charset="utf-8">
<title>Marlow Crest Group – Business Card</title>
<link rel="stylesheet" href="https://fonts.googleapis.com/css2?family=Montserrat:wght@400;500;700&display=swap">
<style>
  :root {
    --canvas: #e9e8e6;
    --card-white: #ffffff;
    --card-white-shade: #e4e4e4;
    --ink: #1b1b1b;
    --ink-soft: #3a3a3a;
    --divider: #c9c9c9;
    --band: #1e1e1e;
    --band-edge: #5a5a5a;
    --back-black: #161616;
    --back-pattern: #232323;
    --on-dark: #f4f4f4;
  }
  * { margin: 0; padding: 0; box-sizing: border-box; }
  html, body { width: 1200px; height: 843px; overflow: hidden; }
  body {
    background: var(--canvas);
    font-family: "Montserrat", sans-serif;
    display: flex;
    align-items: center;
    justify-content: center;
    gap: 50px;
  }
  .card {
    width: 540px;
    height: 310px;
    border-radius: 18px;
    overflow: hidden;
    position: relative;
    box-shadow: 0 10px 30px rgba(0,0,0,0.18);
  }

  /* Back */
  .card-back { background: var(--back-black); }
  .back-texture {
    position: absolute; inset: 0;
    background: radial-gradient(ellipse at 40% 40%, var(--back-pattern), var(--back-black) 75%);
  }
  .back-name {
    position: absolute;
    right: 34px; bottom: 40px;
    display: flex; align-items: center; gap: 10px;
    color: var(--on-dark);
    font-size: 13px; font-weight: 500; letter-spacing: 0.12em;
  }
  .back-name .mark-dot {
    width: 12px; height: 12px; border-radius: 50%;
    border: 1.5px solid var(--on-dark);
  }

  /* Front */
  .card-front {
    background: linear-gradient(160deg, var(--card-white) 40%, var(--card-white-shade));
  }
  .front-body {
    position: absolute; left: 0; right: 0; top: 0; height: 228px;
    display: flex; align-items: center;
  }
  .brand {
    width: 250px;
    display: flex; flex-direction: column; align-items: center; gap: 12px;
  }
  .brand .mark-dot {
    width: 46px; height: 46px; border-radius: 50%;
    border: 2px solid var(--ink-soft);
  }
  .brand-name {
    font-size: 17px; font-weight: 500; letter-spacing: 0.04em;
    color: var(--ink-soft);
    text-align: center;
  }
  .divider {
    width: 1px; height: 120px; background: var(--divider);
  }
  .contact { padding-left: 28px; color: var(--ink); }
  .contact-name {
    font-size: 21px; font-weight: 700; letter-spacing: 0.02em;
    margin-bottom: 14px;
  }
  .contact-line {
    font-size: 12.5px; font-weight: 500; letter-spacing: 0.03em;
    color: var(--ink-soft); line-height: 1.7;
  }
  .contact-line .label { font-weight: 700; color: var(--ink); }
  .web-band {
    position: absolute; left: 0; right: 0; bottom: 0; height: 82px;
    background: var(--band);
    border-top: 4px solid var(--band-edge);
    display: flex; align-items: center; justify-content: center;
    color: var(--on-dark);
    font-size: 14px; font-weight: 500; letter-spacing: 0.2em;
  }
</style>
</head>
<body>
  <section class="card card-back" aria-label="Card back">
    <div class="back-texture" role="img" aria-label="Subtle tonal repeat pattern on black"></div>
    <div class="back-name"><span class="mark-dot"></span>MARLOW CREST GROUP</div>
  </section>

  <section class="card card-front" aria-label="Card front">
    <div class="front-body">
      <div class="brand">
        <span class="mark-dot"></span>
        <span class="brand-name">MARLOW CREST GROUP</span>
      </div>
      <div class="divider"></div>
      <div class="contact">
        <p class="contact-name">GLEN VARLEY</p>
        <p class="contact-line"><span class="label">PHONE :</span> 0437259064</p>
        <p class="contact-line">GLEN@MARLOWCREST-EXAMPLE.COM.AU</p>
      </div>
    </div>
    <div class="web-band">WWW.MARLOWCREST-EXAMPLE.COM.AU</div>
  </section>
</body>
</html>
```